Professional BIO Template with photo and logo

Hello,
I need a professional Bio template developed via Microsoft WORD ASAP!!!!! I would like to just be able to add the text I need to add. So resize-able text boxes. Potentially able to adjust the font. These are the things I need added it to include.
Head shot (attached)
Text Box for Name
Text Box for phone number
Text box for email
KTW Logo (attached)
Maybe a blue banner at the top or some background boxes that are blue or grey. Here are the pantone colors that our company uses.

CORE COLOR
100c 91m 17y 6k 38r 58g 128b Hex #263A80 Pantone 7687 C

CORE CONTRAST COLOR
36c 29m 28y 0k 168r 168g 170b Hex #669999 Pantone Cool Gray 6C

I also attached some examples of what we have been looking at. Instead of green add the blue...instead of black maybe just be white.

Thank you

```html
<!DOCTYPE html>
<html lang="en">
<head>
<meta charset="utf-8">
<title>Marlen Hobbs – Bio</title>
<link href="https://fonts.googleapis.com/css2?family=DM+Serif+Display&family=Open+Sans:wght@400;700&display=swap" rel="stylesheet">
<style>
  :root {
    --core-blue: #263a80;
    --contrast-gray: #7a7a7a;
    --frame-gray: #a8a8aa;
    --ink: #1a1a1a;
    --paper: #ffffff;
    --backdrop: #eeeeee;
  }
  * { margin: 0; padding: 0; box-sizing: border-box; }
  html, body {
    width: 1200px; height: 1200px; overflow: hidden;
    background: var(--backdrop);
  }
  .bio-page {
    position: absolute; left: 176px; top: 0;
    width: 848px; height: 1200px;
    background: var(--paper);
    font-family: "Open Sans", sans-serif;
    color: var(--ink);
    overflow: hidden;
  }
  .top-banner {
    position: absolute; left: 0; top: 0;
    width: 100%; height: 174px;
    background: var(--core-blue);
  }
  .headshot {
    position: absolute; left: 329px; top: 56px;
    width: 190px; height: 190px; border-radius: 50%;
    border: 5px solid var(--paper);
    background: radial-gradient(circle at 50% 40%, #6b6b6b 0%, #4a4a4a 55%, #2f3140 100%);
  }
  .person-name {
    position: absolute; left: 0; top: 252px; width: 100%;
    text-align: center;
    font-family: "DM Serif Display", serif;
    font-size: 52px; line-height: 1.1;
    color: var(--core-blue);
  }
  .person-role {
    position: absolute; left: 0; top: 304px; width: 100%;
    text-align: center;
    font-size: 26px; line-height: 1.2;
  }
  .contact-table {
    position: absolute; left: 88px; top: 355px;
    width: 678px; height: 34px;
    display: flex;
    border: 1.5px solid var(--ink);
  }
  .contact-cell {
    flex: 1; display: flex; align-items: center;
    font-size: 17px;
  }
  .contact-cell + .contact-cell { border-left: 1.5px solid var(--ink); }
  .contact-phone { padding-left: 57px; }
  .contact-email { padding-left: 27px; }
  .contact-cell strong { font-weight: 700; margin-right: 5px; }
  .section-title {
    position: absolute; left: 75px; top: 434px;
    font-family: "DM Serif Display", serif;
    font-size: 35px; line-height: 1;
  }
  .section-rule {
    position: absolute; left: 76px; top: 484px;
    width: 695px; height: 1px; background: #555;
  }
  .section-rule::before {
    content: ""; position: absolute; left: 0; top: -1px;
    width: 50px; height: 3px; background: var(--core-blue);
  }
  .about-text {
    position: absolute; left: 78px; top: 501px; width: 700px;
    font-size: 16.6px; line-height: 25.7px;
  }
  .about-text p span { display: block; white-space: nowrap; }
  .about-text p + p { margin-top: 19px; }
  .about-text p:last-child { margin-top: 24px; }
  .company-mark {
    position: absolute; left: 622px; top: 1014px;
    width: 169px; height: 124px;
    display: flex; align-items: center; justify-content: center; gap: 12px;
  }
  .company-mark .mark-square {
    width: 22px; height: 22px; border: 2px solid var(--frame-gray);
  }
  .company-mark .mark-name {
    font-family: "Open Sans", sans-serif; font-weight: 700;
    font-size: 46px; color: var(--core-blue); letter-spacing: 2px;
  }
  .footer-band {
    position: absolute; left: 0; bottom: 0; width: 848px; height: 39px;
  }
</style>
</head>
<body>
  <main class="bio-page">
    <div class="top-banner"></div>
    <div class="headshot" role="img" aria-label="Headshot portrait of Marlen Hobbs"></div>

    <h1 class="person-name">Marlen Hobbs</h1>
    <p class="person-role">Counsel, Ashford &amp; Lane LLP</p>

    <div class="contact-table">
      <div class="contact-cell contact-phone"><strong>Phone:</strong> 123 456 789</div>
      <div class="contact-cell contact-email"><strong>Email:</strong> youremail@website.com</div>
    </div>

    <h2 class="section-title">About</h2>
    <div class="section-rule"></div>

    <section class="about-text">
      <p>
        <span>Lorem ipsum dolor sit amet, consectetur adipiscing elit, sed do eiusmod tempor incididunt ut</span>
        <span>labore et dolore magna aliqua. Quis ipsum suspendisse ultrices gravida. Risus commodo</span>
        <span>viverra maecenas accumsan lacus vel facilisis. Lorem ipsum dolor sit amet, consectetur</span>
        <span>adipiscing elit, sed do eiusmod tempor incididunt ut labore et dolore magna aliqua. Quis</span>
        <span>ipsum suspendisse ultrices gravida. Risus commodo viverra maecenas</span>
        <span>accumsan lacus vel</span>
      </p>
      <p>
        <span>Lorem ipsum dolor sit amet, consectetur adipiscing elit, sed do eiusmod tempor incididunt ut</span>
        <span>labore et dolore magna aliqua. Quis ipsum suspendisse ultrices gravida. Risus commodo</span>
        <span>viverra maecenas accumsan lacus vel facilisis. Lorem ipsum dolor sit amet, consectetur</span>
        <span>adipiscing elit, sed do eiusmod tempor incididunt ut labore et dolore magna aliqua. Quis</span>
        <span>ipsum suspendisse ultrices gravida. Risus commodo viverra maecenas</span>
        <span>accumsan lacus vel</span>
      </p>
      <p>
        <span>Lorem ipsum dolor sit amet, consectetur adipiscing elit, sed do eiusmod tempor incididunt ut</span>
        <span>labore et dolore magna aliqua. Quis ipsum suspendisse ultrices gravida. Risus commodo</span>
        <span>viverra maecenas accumsan lacus vel facilisis. Lorem ipsum dolor sit amet, consectetur</span>
        <span>adipiscing elit, sed do eiusmod tempor incididunt ut labore et dolore magna aliqua. Quis</span>
        <span>ipsum suspendisse ultrices gravida. Risus commodo viverra maecenas</span>
        <span>accumsan lacus vel</span>
      </p>
    </section>

    <div class="company-mark">
      <span class="mark-square"></span>
      <span class="mark-name">KTW</span>
    </div>

    <svg class="footer-band" viewBox="0 0 848 39" preserveAspectRatio="none">
      <polygon points="0,0 513,0 523,15 848,15 848,39 0,39" fill="var(--contrast-gray)"/>
    </svg>
  </main>
</body>
</html>
```